6 Product labels for a Skincare brand

I have a logo and 6 label templates for 6 skincare productsI need someone to design the product labelsthe design of all 6 labels should be very similar just with basic adjustmentsPlease show me only the design for "Velaquin30ml_Template_V2" and then we can do the others

Target Market(s)

Women +45

Industry/Entity Type

Skin Care Product

Font styles to use
Other font styles liked:
• Helvetica

Colors
ffffff
fef7ee
feeeee
fbe7d2
fefced

Requirements
Must have
• Clean Clean design
• Company details are:
• Distributed by: MARLEE QUINTAV, Lyle, WA 98000
• support@marleequintav.example, (866) 555-0172

```html
<!DOCTYPE html>
<html lang="en">
<head>
<meta charset="utf-8">
<title>Velaquin 30ml Label</title>
<link href="https://fonts.googleapis.com/css2?family=Source+Sans+3:wght@400;500;600;700&display=swap" rel="stylesheet">
<style>
  :root {
    --page: #ffffff;
    --label-bg: #f7e5d1;
    --label-light: #fef7ee;
    --rule: #6b5a4e;
    --dash: #bcd6de;
    --ink: #1d1a17;
    --logo-bg: #ffffff;
  }
  html, body {
    margin: 0;
    width: 1200px;
    height: 1200px;
    overflow: hidden;
    background: var(--page);
    font-family: "Source Sans 3", Helvetica, Arial, sans-serif;
    color: var(--ink);
  }
  .canvas { position: relative; width: 1200px; height: 1200px; }
  .label {
    position: absolute;
    left: 5px; top: 515px;
    width: 1190px; height: 170px;
    border-radius: 18px;
    background: var(--label-bg);
    overflow: hidden;
  }
  .label-pattern {
    position: absolute; inset: 0;
    background: radial-gradient(ellipse 160px 90px at 420px 60px, var(--label-light), transparent 70%),
                radial-gradient(ellipse 170px 90px at 700px 80px, var(--label-light), transparent 70%),
                radial-gradient(ellipse 150px 80px at 1060px 60px, var(--label-light), transparent 70%),
                radial-gradient(ellipse 120px 70px at 120px 40px, var(--label-light), transparent 70%);
    opacity: 0.8;
  }
  .frame {
    position: absolute;
    left: 11px; top: 11px; right: 11px; bottom: 11px;
    border: 1px solid var(--rule);
    border-radius: 6px;
  }
  .safe-line {
    position: absolute;
    left: 22px; top: 22px; right: 22px; bottom: 22px;
    border: 1px dashed var(--dash);
  }
  .panel-left {
    position: absolute; left: 29px; top: 27px; width: 296px;
    font-size: 9.6px; line-height: 13px; font-weight: 500;
  }
  .panel-left p { margin: 0; }
  .panel-left .caution { margin-top: 22px; }
  .panel-left .distributor { margin-top: 14px; font-size: 9.2px; letter-spacing: -0.2px; }
  .panel-left b { font-weight: 700; }
  .lot-code { position: absolute; left: 237px; top: 112px; font-size: 7px; font-weight: 700; }
  .lot-box {
    position: absolute; left: 236px; top: 124px;
    width: 51px; height: 16px;
    background: #ffffff; border: 1px solid #b9aea4;
  }
  .brand-mark {
    position: absolute; left: 512px; top: 38px;
    width: 69px; height: 69px;
    background: var(--logo-bg);
    display: flex; align-items: center; justify-content: center;
    text-align: center;
    font-size: 8px; letter-spacing: 2.6px; line-height: 11px; font-weight: 400;
  }
  .product-name {
    position: absolute; left: 470px; width: 152px; top: 115px;
    text-align: center; font-size: 10px; letter-spacing: 0.3px;
  }
  .product-size {
    position: absolute; left: 470px; width: 152px; top: 131px;
    text-align: center; font-size: 10px;
  }
  .ingredients {
    position: absolute; left: 744px; top: 29px; width: 415px;
    font-size: 8.8px; line-height: 13px; text-align: justify;
    letter-spacing: -0.3px; font-weight: 500;
  }
  .ingredients b { font-weight: 700; }
  .organic-note {
    position: absolute; right: 36px; top: 130px;
    font-size: 8.5px; font-weight: 500;
  }
</style>
</head>
<body>
<div class="canvas">
  <div class="label">
    <div class="label-pattern" role="img" aria-label="Soft cream floral pattern across the label background"></div>
    <div class="frame"></div>
    <div class="safe-line"></div>

    <div class="panel-left">
      <p class="directions"><b>DIRECTIONS:</b> Apply evenly over the face and neck. Use twice daily as part of your anti-aging regime or as needed for added moisture.</p>
      <p class="caution"><b>CAUTION:</b> For external use only. Avoid direct contact with eyes. If irritation occurs, discontinue use.</p>
      <p class="distributor"><b>Distributed By:</b> MARLEE QUINTAV, Lyle, WA 98000<br>support@marleequintav.example, (866) 555-0172</p>
    </div>
    <div class="lot-code">T-V2</div>
    <div class="lot-box"></div>

    <div class="brand-mark">MARLEE<br>QUINTAV</div>
    <div class="product-name">VELAQUIN</div>
    <div class="product-size">30 ml &nbsp;|&nbsp; 1 fl oz</div>

    <div class="ingredients"><b>INGREDIENTS:</b> Water, Prunus Amygdalus Dulcis (Sweet Almond) Oil, Caprylic/Capric Triglyceride, Myristic Acid, Stearic Acid, Cetyl Esters, Glyceryl Stearate SE, Aloe Barbadensis (Aloe Vera) Leaf Juice*, Cetearyl Alcohol, Ceteareth-20, Diheptyl Succinate, Capryloyl Glycerin/Sebacic Acid Copolymer, Pyrus Malus (Apple) Fruit Extract, Glycerin, Dehydroacetic Acid, Benzyl Alcohol, Saccharide Isomerate, Acetyl Hexapeptide-30, Arginine, Caprylyl Glycol, Tromethamine, Carbomer, Potassium Sorbate, Squalane, Tocopheryl Acetate, Ubiquinone, Fagus Sylvatica Bud Extract, Sodium Carboxymethyl Beta-Glucan, Taraxacum Officinale (Dandelion) Leaf Extract, Salvia Officinalis (Sage) Leaf Extract, Melissa Officinalis Leaf Extract, Sodium Benzoate, Citric Acid.</div>
    <div class="organic-note">*Certified Organic Ingredients</div>
  </div>
</div>
</body>
</html>
```